Stationary Design for Norvack Digital

We are after a full stationary back business cards, letterheads, compliment slip, invoice template, delivery note and anything else we could use within the stationary pack.

We would also like an email footer creating.

Our company details to be included on all stationary:

Registered Name: Norvack Limited
Company Registration Number: 20483957
Website: www.norvackdigital.example
email: info@norvackdigital.example
Phone: 01632 960 417
Address: 48 Elmstead Lane Loughborough Leicestershire United Kingdom LE14 7QW

Industry/Entity Type

Business

```html
<!DOCTYPE html>
<html lang="en">
<head>
<meta charset="utf-8">
<title>Norvack Digital – Invoice</title>
<link href="https://fonts.googleapis.com/css2?family=Bebas+Neue&family=Didact+Gothic&display=swap" rel="stylesheet">
<style>
  :root {
    --ink: #1a1a1a;
    --muted: #6f6f6f;
    --accent: #e8412c;
    --header-fill: #b4cfe9;
    --band: #f29c9c;
    --seal: #9b3b3b;
    --seal-rim: #c9a98a;
    --paper: #ffffff;
  }
  * { margin: 0; padding: 0; box-sizing: border-box; }
  html, body { width: 927px; height: 1200px; overflow: hidden; background: var(--paper); }
  body { font-family: "Didact Gothic", sans-serif; color: var(--ink); }
  .invoice { position: relative; width: 927px; height: 1200px; }
  .abs { position: absolute; }

  .brand { left: 98px; top: 176px; width: 240px; display: flex; align-items: center; gap: 10px; }
  .brand-dot { width: 16px; height: 16px; border-radius: 50%; background: var(--ink); flex: none; }
  .brand-name { font-size: 30px; color: var(--ink); white-space: nowrap; }

  .company-details { left: 80px; top: 261px; width: 280px; text-align: center; font-size: 12.5px; line-height: 14.5px; font-style: normal; }
  .company-details .gap { margin-top: 15px; }

  .seal-placeholder {
    left: 689px; top: 138px; width: 113px; height: 113px; border-radius: 50%;
    background: radial-gradient(circle, var(--seal) 0 70%, var(--seal-rim) 72% 100%);
  }

  .meta { left: 573px; font-size: 12.5px; display: flex; align-items: flex-end; }
  .meta .rule { border-bottom: 1.5px solid var(--ink); margin-left: 4px; height: 1px; margin-bottom: 3px; }

  .section-title { left: 68px; top: 374px; font-size: 19px; font-style: italic; font-weight: 400; letter-spacing: 0.5px; }

  table { position: absolute; left: 66px; width: 790px; border-collapse: collapse; border: 2px solid var(--ink); }
  th, td { border: 1.5px solid var(--ink); }
  th { background: var(--header-fill); font-family: "Bebas Neue", sans-serif; font-weight: 400; font-size: 19px; letter-spacing: 0.3px; }
  .client-table { top: 400px; height: 76px; }
  .client-table th { height: 30px; }
  .items-table { top: 496px; height: 352px; }
  .items-table th { height: 37px; }

  .totals { left: 600px; width: 257px; font-family: "Bebas Neue", sans-serif; font-size: 18px; }
  .totals .row { position: absolute; left: 0; width: 257px; height: 20px; }
  .totals .label { position: absolute; right: 169px; bottom: -2px; }
  .totals .rule { position: absolute; left: 88px; right: 0; bottom: 0; border-bottom: 1.5px solid var(--ink); }

  .thanks { left: 74px; top: 870px; font-family: "Bebas Neue", sans-serif; }
  .thanks .big { font-size: 46px; color: var(--accent); line-height: 46px; }
  .thanks .line2 { position: absolute; left: 6px; top: 44px; white-space: nowrap; line-height: 34px; }
  .thanks .line2 .soft { font-size: 26px; color: var(--muted); }
  .thanks .line2 .strong { font-size: 36px; color: #333; margin-left: 4px; }
  .thanks .line3 { position: absolute; left: 90px; top: 80px; white-space: nowrap; font-size: 26px; color: var(--muted); }
  .thanks .line3 .hl { color: var(--accent); }

  .payment-band { left: 54px; top: 1000px; width: 818px; height: 43px; background: var(--band); text-align: center; font-size: 12px; line-height: 13px; padding-top: 8px; color: #333; }
</style>
</head>
<body>
<main class="invoice">

  <div class="abs brand">
    <span class="brand-dot"></span>
    <span class="brand-name">Norvack Digital</span>
  </div>

  <address class="abs company-details">
    <p>48 Elmstead Lane Loughborough</p>
    <p>Leicestershire United Kingdom, LE14 7QW</p>
    <p class="gap">phone: 01632 960 417</p>
    <p>info@norvackdigital.example</p>
    <p>www.norvackdigital.example</p>
    <p>Company Reg #: 20483957</p>
  </address>

  <div class="abs seal-placeholder" role="img" aria-label="Round invoice seal badge"></div>

  <div class="abs meta" style="top:276px"><span>DATE:</span><span class="rule" style="width:183px"></span></div>
  <div class="abs meta" style="top:294px"><span>INVOICE NO.</span><span class="rule" style="width:178px;margin-left:7px"></span></div>
  <div class="abs meta" style="top:314px"><span>INVOICE FOR:</span><span class="rule" style="width:177px"></span></div>

  <h2 class="abs section-title">INVOICE TO:</h2>

  <table class="client-table">
    <thead><tr><th style="width:149px">Name</th><th style="width:223px">Company</th><th>Company Address</th></tr></thead>
    <tbody><tr><td></td><td></td><td></td></tr></tbody>
  </table>

  <table class="items-table">
    <thead><tr><th style="width:441px">Description</th><th style="width:179px">Rate</th><th>Amount</th></tr></thead>
    <tbody><tr><td></td><td></td><td></td></tr></tbody>
  </table>

  <div class="abs totals" style="top:860px">
    <div class="row" style="top:0"><span class="label">Subtotal</span><span class="rule"></span></div>
    <div class="row" style="top:32px"><span class="label">Discount</span><span class="rule"></span></div>
    <div class="row" style="top:63px"><span class="label">Delivery</span><span class="rule"></span></div>
    <div class="row" style="top:94px"><span class="label">Total</span><span class="rule"></span></div>
  </div>

  <div class="abs thanks">
    <div class="big">Thank You</div>
    <div class="line2"><span class="soft">For Your</span><span class="strong">Business</span></div>
    <div class="line3">From the <span class="hl">Norvack Ltd</span> team.</div>
  </div>

  <div class="abs payment-band">
    <p>Please make a bank transfer to Account: ____________________, Sort Code: __ __ __, quoting the invoice number above.</p>
    <p>Alternatively, cheques can be made payable to “Norvack Ltd.” Online payments are coming soon</p>
  </div>

</main>
</body>
</html>
```